Emerging automotive detailing business

I am starting a small automotive detailing business in hopes of becoming a well-known detailer to work on high end cars. I would like a card to reflect the high quality and time I put into my work. The name of the company is Brightmere Detailing. I feel like it represents racecars getting off the line at the drag strip as well as an innuendo of "Off the Charts". I do minor paint correction such as clay barring, multi-step buffing and polishing, waxing, hand washes, etc. I am always striving to learn more and improve my work. My goal is to have total customer satisfaction. This is a female run business but I do not want it to be very girly. Elegant is okay! I have pictures of my personal kestrel attached, they do not need to be incorporated but if you can think of a cool way to use 1 or all of them, go for it!

Target Market(s)

Anyone that owns a vehicle. Preferably high end vehicles such as Valdren, Castavelli and Moretto but I will also happily work on any car, truck or suv no matter what brand.

Industry/Entity Type

Automotive

Contact Information for Business Card

Brightmere Detailing
Nora Pellworth
4715 Quillbrook Rd
Alder Falls NV 89421
Cell phone- call/text- 717-555-0148
email- brightmeredetails@example.com
Instagram: @brightmeredetailing
Facebook: facebook.example/brightmeredetailing

Requirements
Must have
• Business name, my name, address, phone number. Listing that I do minor paint correction such as clay barring, multi-step buffing and polishing, waxing, hand washes, interior cleaning, and more. (This last part was in nice to haves but I have realized that I do really want it, so I moved it to must haves.) I want something that is different and eye-catching to my customers. Some people have done this very well with cards already submitted to me, but a lot have not. I didn't mess with the "look and feel bars" much because because I am pretty open to the overall design as long as it is not your basic run of the mill design.
Nice to have
• Something car related. Maybe an appointment time/date line. I do not have a logo, but if you would like to design one and incorporate it, that would be amazing!
Should not have
• Purple and Pink colors. Boring, basic, normal card.

```html
<!DOCTYPE html>
<html lang="en">
<head>
<meta charset="utf-8">
<title>Brightmere Detailing – Business Card</title>
<link rel="stylesheet" href="https://fonts.googleapis.com/css2?family=Open+Sans:wght@400;600;700&display=swap">
<style>
  :root {
    --page: #e7e4df;
    --ink: #0a0b0d;
    --paper-top: #ffffff;
    --paper-bottom: #e9e9ea;
    --brand-red: #e2262b;
    --brand-blue: #1f86d0;
    --icon-blue: #3aa6e6;
    --text-light: #f3f3f3;
  }
  * { margin: 0; padding: 0; box-sizing: border-box; }
  html, body { width: 1200px; height: 1000px; overflow: hidden; }
  body {
    background: var(--page);
    font-family: "Open Sans", Arial, sans-serif;
    position: relative;
  }
  .card {
    position: absolute;
    width: 709px;
    height: 424px;
    overflow: hidden;
    box-shadow: 0 4px 14px rgba(0,0,0,0.25);
  }
  /* Front */
  .card-front {
    left: 68px; top: 61px;
    background: linear-gradient(var(--paper-top), var(--paper-bottom));
  }
  .front-curve { position: absolute; left: 0; top: 0; }
  .front-brand {
    position: absolute; left: 0; right: 0; top: 146px;
    text-align: center;
    font-weight: 700; font-size: 28px; letter-spacing: 0.5px;
    color: var(--brand-red);
    text-transform: uppercase;
  }
  .brand-dot {
    position: absolute; left: 341px; top: 96px;
    width: 26px; height: 26px; border-radius: 50%;
    background: var(--brand-blue);
  }
  .holder-name {
    position: absolute; left: 0; right: 0; top: 236px;
    text-align: center;
    font-weight: 700; font-size: 24px;
    color: var(--brand-red);
  }
  .contact-list {
    position: absolute; left: 45px; top: 334px;
    list-style: none; color: var(--text-light); font-size: 19px;
  }
  .contact-list li { display: flex; align-items: center; height: 31px; }
  .contact-list svg { width: 20px; height: 20px; margin-right: 14px; }
  .address {
    position: absolute; left: 451px; top: 337px;
    display: flex; color: var(--text-light); font-size: 20px; line-height: 27px;
  }
  .address svg { width: 20px; height: 20px; margin-right: 8px; margin-top: 3px; }
  /* Back */
  .card-back {
    left: 420px; top: 520px;
    background: var(--ink);
    border: 1px solid #3b3b3b;
  }
  .back-brand {
    position: absolute; left: 0; right: 0; top: 200px;
    text-align: center;
    font-weight: 700; font-size: 32px; letter-spacing: 0.5px;
    color: var(--brand-red);
    text-transform: uppercase;
  }
  .back-dot {
    position: absolute; left: 337px; top: 120px;
    width: 34px; height: 34px; border-radius: 50%;
    background: var(--brand-blue);
  }
  .services {
    position: absolute; left: 0; right: 0; top: 273px;
    text-align: center; color: #fff;
    font-weight: 700; font-size: 17.5px; line-height: 27px;
    text-transform: uppercase;
  }
  .services .sep { color: var(--brand-red); margin: 0 4px; }
  .social {
    position: absolute; left: 0; right: 0; top: 372px;
    display: flex; justify-content: center; align-items: center;
    color: var(--text-light); font-size: 19px;
  }
  .social-square {
    width: 24px; height: 24px; border-radius: 3px;
    background: var(--icon-blue); margin-right: 10px;
  }
</style>
</head>
<body>

<section class="card card-front">
  <svg class="front-curve" width="709" height="424" viewBox="0 0 709 424" aria-hidden="true">
    <path d="M0 248 Q354 160 709 248 L709 424 L0 424 Z" fill="var(--ink)"/>
    <path d="M0 246 Q354 158 709 246" fill="none" stroke="var(--brand-blue)" stroke-width="4"/>
  </svg>
  <div class="brand-dot"></div>
  <div class="front-brand">Brightmere Detailing</div>
  <div class="holder-name">Nora Pellworth</div>
  <ul class="contact-list">
    <li>
      <svg viewBox="0 0 20 20" aria-hidden="true"><circle cx="10" cy="10" r="8.5" fill="none" stroke="var(--icon-blue)" stroke-width="1.5"/><path d="M7 5.5l2 2-1 1.2c.6 1.3 1.5 2.2 2.8 2.8l1.2-1 2 2-1.3 1.4c-3.2-.4-6.5-3.7-6.9-6.9z" fill="var(--icon-blue)"/></svg>
      717-555-0148
    </li>
    <li>
      <svg viewBox="0 0 20 20" aria-hidden="true"><rect x="1.5" y="4" width="17" height="12" fill="none" stroke="var(--icon-blue)" stroke-width="1.6"/><path d="M1.5 4l8.5 7 8.5-7" fill="none" stroke="var(--icon-blue)" stroke-width="1.6"/></svg>
      brightmeredetails@example.com
    </li>
  </ul>
  <div class="address">
    <svg viewBox="0 0 20 20" aria-hidden="true"><path d="M10 2L1 10h3v8h4.5v-5h3v5H16v-8h3z" fill="var(--icon-blue)"/></svg>
    <div>4715 Quillbrook Rd<br>Alder Falls NV 89421</div>
  </div>
</section>

<section class="card card-back">
  <div class="back-dot"></div>
  <div class="back-brand">Brightmere Detailing</div>
  <p class="services">
    Clay Barring <span class="sep">•</span> Multi-Step Buffing and Polishing<br>
    Waxing <span class="sep">•</span> Hand Washes Etc
  </p>
  <div class="social"><span class="social-square"></span>@brightmeredetailing</div>
</section>

</body>
</html>
```